Business card design for my trucking company

I would like a business card designed for my new trucking company. Please use my logo. the rest of the design is up to you. i would like my clients to say wow when they see the card. Im looking forward to seeing your designs

Target Market(s)

Industry/Entity Type

Trucking Company

Contact Information for Business Card

Marcus Tillbrook President
518-555-0147
ridgelinehaulingcompany@postvane.com

Font styles to use
Serif

Requirements
Must have
• my logo, name and number. we are located in Schenectady New York. the rest is up to you
Nice to have
• up to you
Should not have
• none

```html
<!DOCTYPE html>
<html lang="en">
<head>
<meta charset="utf-8">
<title>Ridgeline Hauling &amp; Logistics Inc. — Business Card</title>
<link rel="stylesheet" href="https://fonts.googleapis.com/css2?family=Arimo:wght@400;700&display=swap">
<style>
  :root {
    --backdrop: #3b3b3b;
    --card: #232323;
    --red: #e3242b;
    --white: #f2f2f2;
    --grey: #cfcfcf;
  }
  * { box-sizing: border-box; margin: 0; padding: 0; }
  html, body { width: 1200px; height: 801px; overflow: hidden; }
  body {
    background: var(--backdrop);
    font-family: "Arimo", Arial, sans-serif;
    display: flex;
    align-items: center;
    justify-content: center;
    gap: 40px;
  }
  .card {
    width: 540px;
    height: 309px;
    background: var(--card);
    border-bottom: 3px solid var(--red);
    box-shadow: 0 18px 40px rgba(0,0,0,.45);
    position: relative;
  }
  .card-front {
    display: flex;
    align-items: center;
    padding: 0 34px;
  }
  .brand {
    width: 210px;
    color: var(--red);
    font-weight: 700;
    text-transform: uppercase;
    line-height: 1.15;
  }
  .brand-main { display: block; font-size: 34px; letter-spacing: 1px; }
  .brand-sub { display: block; font-size: 11px; letter-spacing: 1.2px; }
  .divider {
    width: 1px;
    height: 96px;
    background: var(--red);
    margin: 0 20px;
  }
  .contact { color: var(--white); }
  .contact-name {
    color: var(--red);
    font-weight: 700;
    font-size: 17px;
    text-transform: uppercase;
  }
  .contact-title { font-size: 12px; color: var(--grey); margin: 3px 0 10px; }
  .contact-line {
    display: flex;
    align-items: center;
    gap: 6px;
    font-size: 11px;
    margin-bottom: 5px;
    white-space: nowrap;
  }
  .contact-line svg { width: 10px; height: 10px; flex: none; }
  .card-back {
    display: flex;
    flex-direction: column;
    justify-content: center;
    padding: 0 44px;
  }
  .back-brand {
    color: var(--red);
    font-weight: 700;
    text-transform: uppercase;
    line-height: 1.1;
  }
  .back-brand .brand-main { font-size: 60px; letter-spacing: 1px; }
  .back-brand .brand-sub { font-size: 17px; letter-spacing: 2px; }
</style>
</head>
<body>
  <section class="card card-front">
    <div class="brand">
      <span class="brand-main">Ridgeline</span>
      <span class="brand-sub">Hauling &amp; Logistics Inc.</span>
    </div>
    <div class="divider"></div>
    <div class="contact">
      <p class="contact-name">Marcus Tillbrook</p>
      <p class="contact-title">President</p>
      <p class="contact-line">
        <svg viewBox="0 0 10 10" aria-hidden="true"><path d="M2 1 L4 3 L3 4 Q4.5 6 6 7 L7 6 L9 8 L8 9 Q4 9 1 5 Q1 3 2 1 Z" fill="var(--red)"/></svg>
        518-555-0147
      </p>
      <p class="contact-line">
        <svg viewBox="0 0 10 10" aria-hidden="true"><rect x="0.5" y="2" width="9" height="6" fill="var(--red)"/><path d="M0.5 2 L5 5.5 L9.5 2" stroke="var(--card)" stroke-width="1" fill="none"/></svg>
        ridgelinehaulingcompany@postvane.com
      </p>
      <p class="contact-line">
        <svg viewBox="0 0 10 10" aria-hidden="true"><circle cx="5" cy="5" r="4.3" fill="none" stroke="var(--red)" stroke-width="1.2"/><path d="M0.7 5 H9.3 M5 0.7 Q2.5 5 5 9.3 M5 0.7 Q7.5 5 5 9.3" stroke="var(--red)" stroke-width=".8" fill="none"/></svg>
        www.ridgelinehauling.com
      </p>
    </div>
  </section>

  <section class="card card-back">
    <div class="back-brand">
      <span class="brand-main">Ridgeline</span>
      <span class="brand-sub">Hauling &amp; Logistics Inc.</span>
    </div>
  </section>
</body>
</html>
```